Lotvantage.com Webpage Design

Design Brief for lotvantage.com (Copy of Brief also in attached Word file)

Name of Website- lotvantage.com (existing logo and look & feel of website to be changed)

Logo - Finalised. The logo files are attached with the brief as “logo.jpeg”. The “Blue- Grey” version of the logo is for use on lighter backgrounds and the “Orange-White” version of the logo is for use on darker backgrounds. (A full Black version of the logo is also attached). Both versions may be used in different parts of the website. All attached files are in .png format.
Status - The website in functional and is undergoing user trials. However, we want to improve the look & feel of the website so at it seems
a. cotemporary,
b. Easy to Navigate
c. professional and
d. Vibrant.

Please visit ‘lotvantage.com’ to check out the website and its functionalities – please use it only as a reference for the features & functions to be provided, however the designer should use a ‘Free Hand’ in designing the composition of various parts of the webpage without getting too influenced by the existing design

Objective of the Website ‘lotvantage.com –
a. It is a portal focussed on listing of ‘Retail’ specific real-estate properties by developers, owners and realty brokers. The properties shall listed under the following four categories-
i. Retail Malls
ii. Shopping Complexes
iii. High-street shops
iv. Retail Warehouses
*refer lotvantage.com for better clarity

b. The abovementioned properties shall be listed either for ‘Sale’ or ‘rent\lease’ or both

c. Users shall visit the site in case they wish to acquire a retail \ shop space either on ‘sale’ or ‘rent’. These Users would be able to specify the ‘Search Criteria’ through the tool-bars provided on the website – the ‘Search Criteria’ shall comprise of ‘Type of space category’, ‘City’, ‘Locality’, transaction type ie ‘Rent \ Sale’ and ‘Area Range’

d. The main revenue model for the website shall be listing fee ( or advertising charges ) payable by those listing their properties on the website.

Three Main Pages of Website (lotvantage.com) that need to be designed -
a. Main Home Page (visit the web link - http://lotvantage.com/ ) - The main home page has the “Search Toolbar” for specifying of Search Criteria by the User. It shall also have the following features & functions-
i. Main Advertising Banner
ii. Featured Projects
iii. New Launches
iv. Toolbar with buttons – ‘Advertise with Us’, ‘Listings Alert’, ‘Lot Mavens’, ‘Advertiser Login’

b. Property Listings Page (visit the web link - http://lotvantage.com/gurgaon-in-india ) - The List of property options that match the Criteria specified by the ‘User’ get displayed on this page.

c. Property Detail Page - When the ‘User’ clicks on the “More….” Button on the ‘Property Listings Page’ (given in point b. above) the web page with the details of the property opens. (For Example – visit the web link - http://lotvantage.com/brevo-Shopping-Complex-brevo-quadrel-gurgaon-636 )

Note:- Please refer to attached ‘Shopping’ related images the designer may use them on the website to provide a look & feel of retail if required – either separately or rotate in a single window

Target Market(s)

Retailers & Investors looking for retail space, Real Estate Brokers, Developers

Industry/Entity Type

Advertising

Number of Pages Required

3 page

Requirements
Must have
• Refer to existing site lotvantage.com -- all the existing functionalities are a must have.
Nice to have
• The Designer may use the retail related images on the website if required for making it more vibrant. Refer attached images Shopping(1-6).jpg

```html
<!DOCTYPE html>
<html lang="en">
<head>
<meta charset="utf-8">
<title>Lotvantage.com – Retail Space Portal</title>
<link rel="stylesheet" href="https://fonts.googleapis.com/css2?family=Open+Sans:wght@400;600;700&family=Noto+Serif&family=Josefin+Sans:wght@300;400&display=swap">
<style>
:root{
  --orange:#e08a2a;
  --orange-light:#eb9a3a;
  --orange-dark:#c9731c;
  --paper:#ebe8e3;
  --white:#ffffff;
  --ink:#3d3d3d;
  --stat-bg:#ececec;
  --wood-dark:#6f4526;
  --wood-mid:#8f5f38;
  --footer-dark:#3b3b3b;
  --btn-dark:#2a2a2a;
  --rule:#c9c6c1;
  --blue-grey:#5a6770;
}
*{box-sizing:border-box;margin:0;padding:0}
html,body{width:760px;height:1200px;overflow:hidden}
body{font-family:"Open Sans",Arial,sans-serif;color:var(--ink);background:var(--paper)}
.page{position:relative;width:760px;height:1200px;overflow:hidden;background:var(--paper)}
.abs{position:absolute}

/* header */
.site-header{left:0;top:0;width:760px;height:77px;background:#f3f2f0}
.brand{left:66px;top:22px;display:flex;align-items:center;gap:8px}
.brand-dot{width:22px;height:22px;border-radius:50%;background:var(--orange);flex-shrink:0}
.brand-name{font-weight:700;font-size:26px;color:var(--blue-grey);letter-spacing:-.5px}
.contact{right:66px;top:14px;display:flex;gap:14px;font-size:9px;font-weight:600;color:#333;align-items:center;border-bottom:1px solid #aaa;padding:0 0 4px 6px}
.contact span{display:flex;align-items:center;gap:5px}
.nav{right:66px;top:42px;display:flex;gap:34px;align-items:center;font-size:10px;color:#333}
.nav .active{background:var(--orange);color:#fff;padding:3px 12px;border-radius:10px}

/* hero */
.hero{left:0;top:77px;width:760px;height:251px;background:linear-gradient(90deg,var(--wood-dark) 0%,var(--wood-mid) 30%,#9a6840 55%,var(--wood-mid) 78%,var(--wood-dark) 100%)}
.hero-line{left:0;top:326px;width:760px;height:4px;background:var(--orange)}
.hero-frame{left:75px;top:105px;width:611px;height:241px;background:#fff;padding:6px}
.hero-photo{width:100%;height:100%;background:linear-gradient(110deg,#5e4434 0%,#b8493a 20%,#d9b84a 38%,#a79a8c 58%,#5d6f86 78%,#c9a894 100%)}
.search-panel{left:115px;top:293px;width:532px;height:90px;background:linear-gradient(var(--orange-light),var(--orange-dark));border-radius:3px;box-shadow:0 3px 6px rgba(0,0,0,.25)}
.search-title{position:absolute;left:0;top:8px;width:100%;text-align:center;font-family:"Josefin Sans",sans-serif;font-weight:300;font-size:19px;color:#3a2410}
.search-title::before,.search-title::after{content:"";position:absolute;top:12px;width:120px;height:3px;border-top:1px solid rgba(255,255,255,.6);border-bottom:1px solid rgba(255,255,255,.6)}
.search-title::before{left:15px}
.search-title::after{right:15px}
.search-row{position:absolute;left:15px;top:46px;display:flex;gap:10px}
.field{height:20px;background:#f3f3f3;border:1px solid #d6d6d6;font-size:8px;color:#333;display:flex;align-items:center;justify-content:space-between;padding:0 4px}
.field.select{width:75px}
.field .arrow{width:10px;height:10px;border:1px solid #555;display:flex;align-items:center;justify-content:center}
.field.input{width:73px;color:#aaa}
.search-btn{width:74px;height:20px;background:linear-gradient(#777,#4a4a4a);color:#fff;font-size:8px;font-weight:700;display:flex;align-items:center;justify-content:center;border-radius:2px;margin-left:6px}

/* featured */
.section-title{left:62px;top:408px;width:632px;text-align:center;font-weight:700;font-size:18px;color:#222}
.section-title::before,.section-title::after{content:"";position:absolute;top:13px;width:210px;height:3px;border-top:1px solid var(--rule);border-bottom:1px solid var(--rule)}
.section-title::before{left:0}
.section-title::after{right:0}
.listing-board{left:64px;top:457px;width:416px;height:471px;background:#fff;border-radius:4px}
.listing{position:absolute;width:188px}
.listing h3{font-family:"Noto Serif",serif;font-weight:400;font-size:10.5px;color:#444;white-space:nowrap}
.listing-photo{margin-top:6px;height:111px}
.photo-building{background:linear-gradient(#7db8e6 0%,#b9c3c0 30%,#c4b48f 55%,#7f968a 85%,#5f7466 100%)}
.photo-atrium{background:linear-gradient(#786a5e 0%,#b9a88f 40%,#8f8a74 75%,#5f5a4c 100%)}
.photo-aerial{background:linear-gradient(#86bde8 0%,#c3c8cb 35%,#a3a58e 65%,#6f7f5f 100%)}
.stats{height:24px;background:var(--stat-bg);display:flex;justify-content:space-around;align-items:center;font-size:7.5px;color:#777}
.stats span{display:flex;align-items:center;gap:3px}
.listing p{margin-top:10px;font-size:7.5px;line-height:12px;color:#555}
.board-rule{position:absolute;left:13px;width:390px;height:1px;background:#ddd}
.pager{position:absolute;left:13px;top:440px;display:flex;gap:6px}
.pager span{width:18px;height:18px;border-radius:50%;font-size:7px;display:flex;align-items:center;justify-content:center}
.pager .on{background:#333;color:#fff}
.pager .off{background:#ccc;color:#333}

.project-card{position:absolute;left:493px;width:201px;height:92px;background:#fff;border:1px solid #d8d6d2;border-radius:3px}
.project-photo{position:absolute;left:8px;top:8px;width:101px;height:76px;background:linear-gradient(#3f8fd6,#9fcbef 55%,#a9b7b2 80%,#7a9a6e)}
.project-info{position:absolute;left:117px;top:7px;font-size:7.5px;font-weight:700;color:#222;line-height:14px}
.project-info h4{font-size:12.5px;font-weight:600;color:#444;line-height:18px}
.project-btn{display:inline-block;margin-top:2px;background:var(--orange);color:#fff;font-size:7.5px;padding:1px 8px;line-height:13px}

/* footer */
.footer{left:0;top:957px;width:760px;height:181px;background:linear-gradient(var(--orange-light),var(--orange-dark))}
.footer-col{position:absolute;top:18px;color:#1d1d1d}
.footer-col h5{font-size:13px;font-weight:700;margin-bottom:8px;color:#1a1a1a}
.footer-divider{position:absolute;top:10px;width:1px;height:162px;background:rgba(255,255,255,.5)}
.alert-row{display:flex;gap:8px;font-size:7.5px;line-height:11px}
.alert-row svg{flex-shrink:0}
.email-field{position:absolute;background:#fff;border:1px solid #ddd;height:20px;font-size:7.5px;color:#999;padding:4px 5px}
.dark-btn{position:absolute;background:var(--btn-dark);color:#fff;font-weight:700;font-size:11px;border-radius:3px;display:flex;align-items:center;justify-content:center;border:1px solid #111}
.editor-text{font-size:7.5px;line-height:13px;width:212px}
.bottom-bar{left:0;top:1138px;width:760px;height:62px;background:var(--footer-dark);color:#ddd;font-size:8px;line-height:16px}
.bottom-bar .legal{position:absolute;left:61px;top:14px}
.bottom-bar .brand-foot{position:absolute;right:66px;top:15px;display:flex;align-items:center;gap:7px}
.brand-foot .brand-dot{width:20px;height:20px}
.brand-foot .brand-name{color:#fff;font-size:22px}
</style>
</head>
<body>
<div class="page">

  <header class="site-header abs">
    <div class="brand abs"><span class="brand-dot"></span><span class="brand-name">lotvantage.com</span></div>
    <div class="contact abs">
      <span><svg width="11" height="9" viewBox="0 0 11 9"><rect x=".5" y=".5" width="10" height="7" rx="1.5" fill="none" stroke="#8b1a1a"/><path d="M3 4h5" stroke="#8b1a1a"/></svg>info@lotvantage.com</span>
      <span><svg width="10" height="10" viewBox="0 0 10 10"><circle cx="5" cy="5" r="4.5" fill="none" stroke="#8b1a1a"/><path d="M3.3 2.8c0 2.2 1.7 4 3.6 4" stroke="#8b1a1a" fill="none" stroke-width="1.3"/></svg>555 014 2286</span>
    </div>
    <nav class="nav abs">
      <span class="active">Home ⌄</span><span>Advertise with us</span><span>Lot Mavens</span><span>Listing Alert</span>
    </nav>
  </header>

  <section class="hero abs" role="img" aria-label="Warm wood panelling backdrop"></section>
  <div class="hero-line abs"></div>
  <div class="hero-frame abs"><div class="hero-photo" role="img" aria-label="Shoppers looking at a store window display with sale signs and a red handbag"></div></div>

  <form class="search-panel abs">
    <div class="search-title">Meaning of Retail Format</div>
    <div class="search-row">
      <div class="field select">Type<span class="arrow"><svg width="6" height="4"><path d="M0 0h6L3 4z" fill="#333"/></svg></span></div>
      <div class="field select">-Select-<span class="arrow"><svg width="6" height="4"><path d="M0 0h6L3 4z" fill="#333"/></svg></span></div>
      <div class="field select">-Select-<span class="arrow"><svg width="6" height="4"><path d="M0 0h6L3 4z" fill="#333"/></svg></span></div>
      <div class="field input">Min price</div>
      <div class="field input">Max price</div>
      <div class="search-btn">SEARCH</div>
    </div>
  </form>

  <h2 class="section-title abs">Featured Retail Projects</h2>

  <section class="listing-board abs">
    <article class="listing" style="left:13px;top:14px">
      <h3>412 Harbor Lane, Palm Reach, FL</h3>
      <div class="listing-photo photo-building" role="img" aria-label="Modern beige retail building with glass shopfronts"></div>
      <div class="stats"><span>⌂ 5000 Sq ft.</span><span>▭ 4 Beds</span><span>◔ 3 Baths</span></div>
      <p>Lorem ipsum dolor sit amet, consectetuer adipiscing elit, sed diam nonummy nibh euismod tincidunt ut...</p>
    </article>
    <article class="listing" style="left:214px;top:14px">
      <h3>2208 Sunline Blvd, Westmere, FL</h3>
      <div class="listing-photo photo-atrium" role="img" aria-label="Busy shopping mall atrium with palm trees and shoppers"></div>
      <div class="stats"><span>⌂ 5000 Sq ft.</span><span>▭ 4 Beds</span><span>◔ 3 Baths</span></div>
      <p>Lorem ipsum dolor sit amet, consectetuer adipiscing elit, sed diam nonummy nibh euismod tincidunt ut...</p>
    </article>
    <div class="board-rule" style="top:213px"></div>
    <article class="listing" style="left:13px;top:231px">
      <h3>1740 Orchard Ave, Cedar Cove</h3>
      <div class="listing-photo photo-aerial" role="img" aria-label="Aerial view of a large shopping complex with parking"></div>
      <div class="stats"><span>⌂ 1200 Sq ft.</span><span>▭ 2 Beds</span><span>◔ 2 Baths</span></div>
      <p>Lorem ipsum dolor sit amet, consectetuer adipiscing elit, sed diam nonummy nibh euismod tincidunt ut...</p>
    </article>
    <article class="listing" style="left:214px;top:231px">
      <h3>960 Marlowe Ave Bay Terrace, FL</h3>
      <div class="listing-photo photo-building" role="img" aria-label="Modern beige retail building with glass shopfronts"></div>
      <div class="stats"><span>⌂ 3500 Sq ft.</span><span>▭ 5 Beds</span><span>◔ 4 Baths</span></div>
      <p>Lorem ipsum dolor sit amet, consectetuer adipiscing elit, sed diam nonummy nibh euismod tincidunt ut...</p>
    </article>
    <div class="board-rule" style="top:426px"></div>
    <div class="pager"><span class="on">1</span><span class="off">2</span></div>
  </section>

  <aside>
    <div class="project-card" style="top:459px">
      <div class="project-photo" role="img" aria-label="Glass high-rise towers under blue sky"></div>
      <div class="project-info"><h4>Gurgaon</h4>Norvik Centrum<br>Sector-65<br>Shopping Complex<br><span class="project-btn">View Property</span></div>
    </div>
    <div class="project-card" style="top:574px">
      <div class="project-photo" role="img" aria-label="Glass high-rise towers under blue sky"></div>
      <div class="project-info"><h4>Gurgaon</h4>Norvik Centrum<br>Sector-65<br>Shopping Complex<br><span class="project-btn">View Property</span></div>
    </div>
    <div class="project-card" style="top:689px">
      <div class="project-photo" role="img" aria-label="Glass high-rise towers under blue sky"></div>
      <div class="project-info"><h4>Gurgaon</h4>Norvik Centrum<br>Sector-65<br>Shopping Complex<br><span class="project-btn">View Property</span></div>
    </div>
  </aside>

  <footer class="footer abs">
    <div class="footer-col" style="left:66px;width:152px">
      <h5>Listing Alert</h5>
      <div class="alert-row">
        <svg width="38" height="38" viewBox="0 0 38 38"><path d="M2 14L19 2l17 12v22H2z" fill="#2f7fc1"/><path d="M2 14h34v22H2z" fill="#4a4a4a"/><path d="M2 14l17 12 17-12" fill="none" stroke="#ddd" stroke-width="1.5"/><text x="19" y="18" font-size="10" text-anchor="middle" fill="#e08a2a" font-family="Arial">@</text></svg>
        <span>Suscribe for Fortnightly Email update on New Listings @ Lotvantage</span>
      </div>
    </div>
    <div class="email-field" style="left:66px;top:88px;width:152px">Email Your Email Address:</div>
    <div class="dark-btn" style="left:153px;top:120px;width:65px;height:22px">Subscribe</div>
    <div class="footer-divider" style="left:233px"></div>
    <div class="footer-col" style="left:252px">
      <h5>Editor's Choice</h5>
      <p class="editor-text">A "Select" Listing of Retail Properties Handpicked by our Editors based on their own positive evaluation on parameters &amp; attributes such as Design Concept, Location, Developer, Success Potential. So Read On to Check Out for yourself ............ ..</p>
    </div>
    <div class="footer-divider" style="left:486px"></div>
    <div class="footer-col" style="left:525px;width:165px">
      <h5>Lot Mavens</h5>
    </div>
    <div class="email-field" style="left:525px;top:45px;width:165px">Email Your Email Address:</div>
    <div class="email-field" style="left:525px;top:75px;width:165px;height:36px">Add Description of Requirement</div>
    <div class="dark-btn" style="left:625px;top:120px;width:65px;height:22px;font-size:12px">Send</div>
  </footer>

  <div class="bottom-bar abs">
    <div class="legal">Copyright © 2014 . lotvantage All rights reserved.<br>website by Quillon Technologies.</div>
    <div class="brand-foot"><span class="brand-dot"></span><span class="brand-name">lotvantage.com</span></div>
  </div>

</div>
</body>
</html>
```